GDFH Business Card

Looking for a business card design to incorporate our branding. We want to only use the colors listing in the Branding Package (attached).
Updates

Target Market(s)

People who need their phone or device fixed.

Industry/Entity Type

Electronics

Contact Information for Business Card

Please use:

Gadget Fix Haven LLC
4870 S Ridgecrest Pkwy
Suite 318
San Antonio, TX 78291

Wendell Thorsby, Store Manager

(210) 555-0147

Requirements
Must have
• Must include the colors that are contained within the Branding Package PDF file.

```html
<!DOCTYPE html>
<html lang="en">
<head>
<meta charset="utf-8">
<title>Gadget Fix Haven Business Card</title>
<link rel="stylesheet" href="https://fonts.googleapis.com/css2?family=Arimo:wght@400&display=swap">
<style>
  :root {
    --bg: #5f5f5f;
    --brand-orange: #f05423;
    --card-white: #ffffff;
    --text-grey: #6b6b6b;
    --text-dark: #3a3a3a;
  }
  html, body {
    margin: 0;
    padding: 0;
    width: 1200px;
    height: 1082px;
    overflow: hidden;
    background: var(--bg);
    font-family: "Arimo", Arial, sans-serif;
  }
  .canvas {
    position: relative;
    width: 1200px;
    height: 1082px;
  }
  .card {
    position: absolute;
    width: 604px;
    height: 338px;
    border-radius: 22px;
    box-sizing: border-box;
  }
  .card-front {
    left: 298px;
    top: 190px;
    background: var(--card-white);
  }
  .card-back {
    left: 300px;
    top: 578px;
    background: var(--brand-orange);
  }
  .card-frame {
    position: absolute;
    inset: 6px;
    border-radius: 18px;
    border: 2px solid var(--brand-orange);
  }
  .card-back .card-frame {
    border-color: var(--card-white);
  }
  .brand {
    position: absolute;
    left: 0;
    right: 0;
    display: flex;
    align-items: center;
    justify-content: center;
    gap: 14px;
  }
  .card-front .brand { top: 84px; }
  .card-back .brand { top: 146px; }
  .brand-square {
    width: 46px;
    height: 46px;
    border-radius: 6px;
    background: var(--brand-orange);
  }
  .card-back .brand-square { background: var(--card-white); }
  .brand-name {
    font-size: 34px;
    color: var(--brand-orange);
    letter-spacing: 0.5px;
  }
  .card-back .brand-name { color: var(--card-white); }
  .person {
    position: absolute;
    left: 36px;
    top: 236px;
  }
  .person-name {
    font-size: 23px;
    color: var(--brand-orange);
    margin: 0 0 6px;
  }
  .person-title {
    font-size: 17px;
    color: var(--text-grey);
    margin: 0 0 6px;
    letter-spacing: 0.3px;
  }
  .person-phone {
    font-size: 16px;
    color: var(--text-dark);
    margin: 0;
  }
  .person-phone .label { color: var(--brand-orange); }
  .address {
    position: absolute;
    right: 32px;
    top: 236px;
    text-align: right;
    font-size: 15.5px;
    line-height: 25px;
    color: var(--text-dark);
    font-style: normal;
  }
</style>
</head>
<body>
<div class="canvas">
  <section class="card card-front">
    <div class="card-frame"></div>
    <div class="brand">
      <span class="brand-square"></span>
      <span class="brand-name">Gadget Fix Haven</span>
    </div>
    <div class="person">
      <p class="person-name">Wendell Thorsby</p>
      <p class="person-title">Store Manager</p>
      <p class="person-phone"><span class="label">Phone:</span> (210) 555-0147</p>
    </div>
    <address class="address">
      4870 S Ridgecrest Pkwy<br>
      Suite 318<br>
      San Antonio, TX 78291
    </address>
  </section>
  <section class="card card-back">
    <div class="card-frame"></div>
    <div class="brand">
      <span class="brand-square"></span>
      <span class="brand-name">Gadget Fix Haven</span>
    </div>
  </section>
</div>
</body>
</html>
```